Need CATCHY/VIVID Banner design for my new UTV/ATV/Off Road Vehicle turn signal/lighting company

I need a banner ad designed so I can advertise on several different ATV (all terrain vehicle), UTV (Utility Vehicles), Golf Cart and Off-Road Vehicle forums. Ads need to be very catchy and produce a call to action. Action is getting hits to my website. Our main business is selling turn signal kits to make your side by side or your ATV/UTV street legal, as some states now allow you to drive these on public roads if you have the following items: Turn Signals, Horn, Lighted license plate bracket, headlights and brake lights. We sell all of these items for just about any model vehicle out there. Our call to action for this banner would be to get more website visits.

Target Market(s)

Off-road/outdoor enthusiasts,

Industry/Entity Type

Car Accessorie

Font styles to use
Sans Serif

Requirements
Must have
• Ad size need to be either 728x90 or 300x250. Colorful ad with an off-road vehicle integrated to the design (think UTV, side-by-side, etc.
Nice to have
• Nice to haves would be anything that makes this banner ad stand out on very boring web pages.
Should not have
• anything dull

```html
<!DOCTYPE html>
<html lang="en">
<head>
<meta charset="utf-8">
<title>Turn Signal Kits – Banner Concepts</title>
<link href="https://fonts.googleapis.com/css2?family=Montserrat:wght@500;700;800;900&display=swap" rel="stylesheet">
<style>
  :root {
    --board: #e9e9ea;
    --red: #e3051b;
    --red-deep: #a10018;
    --orange: #f26a1b;
    --yellow: #ffcc00;
    --white: #ffffff;
    --ink: #111111;
    --sand: #c9a57c;
    --rock: #8a6a4c;
    --sky: #b9cfe2;
  }
  * { margin: 0; padding: 0; box-sizing: border-box; }
  html, body { width: 1200px; height: 2188px; overflow: hidden; background: var(--board); }
  body { position: relative; font-family: "Montserrat", Arial, sans-serif; }

  .banner {
    position: absolute; left: 56px; width: 1088px; height: 612px;
    overflow: hidden; background: var(--white);
  }
  .banner--one { top: 88px; }
  .banner--two { top: 788px; }
  .banner--three { top: 1488px; }

  .banner__shapes { position: absolute; inset: 0; width: 100%; height: 100%; }

  .brand {
    position: absolute; display: flex; align-items: center; gap: 12px;
    color: var(--white); font-weight: 800; font-size: 22px; letter-spacing: 0.5px;
    text-transform: uppercase;
  }
  .brand__dot { width: 26px; height: 26px; border-radius: 50%; background: var(--yellow); }

  .headline {
    position: absolute; color: var(--white); font-weight: 900;
    font-size: 46px; line-height: 1.08; text-transform: uppercase; letter-spacing: 1px;
  }
  .lead {
    position: absolute; color: var(--white); font-weight: 700;
    font-size: 17px; line-height: 1.4; width: 330px;
  }
  .cta {
    position: absolute; display: flex; align-items: center; gap: 10px;
    height: 58px; padding: 0 34px 0 30px; background: var(--yellow);
    clip-path: polygon(10px 0, 100% 0, calc(100% - 10px) 100%, 0 100%);
    color: var(--ink); font-weight: 800; font-size: 16px; text-transform: uppercase;
  }
  .cta__icon {
    width: 20px; height: 20px; border-radius: 50%; background: var(--ink);
    display: flex; align-items: center; justify-content: center;
  }

  .banner--one .brand, .banner--three .brand { left: 48px; top: 34px; }
  .banner--one .headline, .banner--three .headline { left: 48px; top: 204px; }
  .banner--one .lead, .banner--three .lead { left: 48px; top: 318px; }
  .banner--one .cta, .banner--three .cta { left: 48px; top: 412px; }

  .banner--two .brand { left: 56px; top: 80px; }
  .banner--two .headline { left: 56px; top: 222px; }
  .banner--two .lead { left: 56px; top: 336px; }
  .banner--two .cta { left: 56px; top: 420px; }
</style>
</head>
<body>

<!-- Banner one: red panel with off-road photo -->
<section class="banner banner--one">
  <svg class="banner__shapes" viewBox="0 0 1088 612" preserveAspectRatio="none">
    <defs>
      <linearGradient id="photoOne" x1="0" y1="0" x2="0" y2="1">
        <stop offset="0" stop-color="var(--sky)"/>
        <stop offset="0.3" stop-color="#b79a7a"/>
        <stop offset="0.7" stop-color="var(--rock)"/>
        <stop offset="1" stop-color="var(--sand)"/>
      </linearGradient>
    </defs>
    <rect x="380" y="0" width="708" height="612" fill="url(#photoOne)" role="img" aria-label="Photo of a red side-by-side UTV climbing desert rocks"/>
    <polygon points="0,0 440,0 392,612 0,612" fill="var(--red)"/>
    <polygon points="412,420 440,420 392,612 364,612" fill="var(--yellow)"/>
    <polygon points="440,0 452,0 404,612 392,612" fill="var(--yellow)" opacity="0"/>
  </svg>
  <div class="brand"><span class="brand__dot"></span>TrailLite Signals</div>
  <h2 class="headline">Turn Signal<br>Kits</h2>
  <p class="lead">Lorem ipsum dolor sit amet, consectetur adipiscing elit, sed do eiusmod</p>
  <a class="cta">Get Started <span class="cta__icon"><svg width="10" height="10" viewBox="0 0 10 10"><path d="M3 1.5 6.5 5 3 8.5" fill="none" stroke="#ffcc00" stroke-width="2"/></svg></span></a>
</section>

<!-- Banner two: red field with vehicle in white circle -->
<section class="banner banner--two">
  <svg class="banner__shapes" viewBox="0 0 1088 612" preserveAspectRatio="none">
    <defs>
      <linearGradient id="redTwo" x1="0" y1="0" x2="1" y2="1">
        <stop offset="0" stop-color="var(--red)"/>
        <stop offset="1" stop-color="var(--red-deep)"/>
      </linearGradient>
      <radialGradient id="vehicleTwo" cx="0.5" cy="0.5" r="0.6">
        <stop offset="0" stop-color="#4a4a4a"/>
        <stop offset="1" stop-color="#1e1e1e"/>
      </radialGradient>
    </defs>
    <rect width="1088" height="612" fill="url(#redTwo)"/>
    <circle cx="900" cy="290" r="372" fill="var(--yellow)"/>
    <circle cx="924" cy="272" r="362" fill="var(--white)"/>
    <rect x="620" y="120" width="468" height="330" rx="40" fill="url(#vehicleTwo)" role="img" aria-label="Black four-seat utility side-by-side vehicle"/>
  </svg>
  <div class="brand"><span class="brand__dot"></span>TrailLite Signals</div>
  <h2 class="headline">Turn Signal<br>Kits</h2>
  <p class="lead">Lorem ipsum dolor sit amet, consectetur adipiscing elit, sed do eiusmod</p>
  <a class="cta">Get Started <span class="cta__icon"><svg width="10" height="10" viewBox="0 0 10 10"><path d="M3 1.5 6.5 5 3 8.5" fill="none" stroke="#ffcc00" stroke-width="2"/></svg></span></a>
</section>

<!-- Banner three: red-to-yellow gradient panel with off-road photo -->
<section class="banner banner--three">
  <svg class="banner__shapes" viewBox="0 0 1088 612" preserveAspectRatio="none">
    <defs>
      <linearGradient id="photoThree" x1="0" y1="0" x2="0" y2="1">
        <stop offset="0" stop-color="var(--sky)"/>
        <stop offset="0.3" stop-color="#b79a7a"/>
        <stop offset="0.7" stop-color="var(--rock)"/>
        <stop offset="1" stop-color="var(--sand)"/>
      </linearGradient>
      <linearGradient id="panelThree" x1="0" y1="1" x2="1" y2="0">
        <stop offset="0" stop-color="var(--red)"/>
        <stop offset="0.55" stop-color="var(--orange)"/>
        <stop offset="1" stop-color="var(--yellow)"/>
      </linearGradient>
    </defs>
    <rect x="380" y="0" width="708" height="612" fill="url(#photoThree)" role="img" aria-label="Photo of a red side-by-side UTV climbing desert rocks"/>
    <path d="M0,0 H470 C430,200 420,400 440,612 H0 Z" fill="url(#panelThree)"/>
  </svg>
  <div class="brand"><span class="brand__dot"></span>TrailLite Signals</div>
  <h2 class="headline">Turn Signal<br>Kits</h2>
  <p class="lead">Lorem ipsum dolor sit amet, consectetur adipiscing elit, sed do eiusmod</p>
  <a class="cta">Get Started <span class="cta__icon"><svg width="10" height="10" viewBox="0 0 10 10"><path d="M3 1.5 6.5 5 3 8.5" fill="none" stroke="#ffcc00" stroke-width="2"/></svg></span></a>
</section>

</body>
</html>
```